Ostrel Appraisals BV business cards (a financial services company)

I am looking for a business card design that stands out in the financial advisory field of business & intellectual property valuation. The business card design should be conservative, yet different. Address details have changed since the attached business card. New address is:

Molenvlietkade 27
4817 KT Leiden
The Netherlands

Telephone number remains the same.

```html
<!DOCTYPE html>
<html lang="en">
<head>
<meta charset="utf-8">
<title>Ostrel Appraisals BV – Business Cards</title>
<link href="https://fonts.googleapis.com/css2?family=Roboto:wght@300;400;500;700&display=swap" rel="stylesheet">
<style>
  :root {
    --backdrop: #5b3f2f;
    --card: #ffffff;
    --ink: #777777;
    --ink-strong: #6e6e6e;
    --rule: #6e6e6e;
    --frame: #7a7a7a;
  }
  * { margin: 0; padding: 0; box-sizing: border-box; }
  html, body {
    width: 1200px; height: 1200px; overflow: hidden;
    background: var(--backdrop);
    font-family: "Roboto", Arial, sans-serif;
    color: var(--ink);
  }
  .card {
    position: absolute;
    left: 196px; width: 810px; height: 462px;
    background: var(--card);
    border-radius: 40px;
    box-shadow: 0 6px 14px rgba(0,0,0,0.35);
  }
  .card--front { top: 96px; }
  .card--back { top: 605px; }

  .brand-square {
    position: absolute;
    background: var(--frame);
  }
  .card--front .brand-square { left: 375px; top: 136px; width: 60px; height: 60px; }
  .card--back .brand-square { left: 550px; top: 46px; width: 48px; height: 48px; }

  .brand-frame {
    position: absolute;
    display: flex; align-items: center; justify-content: center;
    border: 4px solid var(--frame);
  }
  .card--front .brand-frame { left: 134px; top: 249px; width: 542px; height: 90px; }
  .card--back .brand-frame { left: 385px; top: 126px; width: 379px; height: 63px; border-width: 3px; }

  .brand-name {
    font-weight: 400;
    color: var(--ink);
    white-space: nowrap;
    letter-spacing: 0.01em;
    line-height: 1;
  }
  .card--front .brand-name { font-size: 44px; }
  .card--back .brand-name { font-size: 30px; }

  .holder {
    position: absolute;
    left: 38px; top: 312px;
  }
  .holder__name {
    font-size: 25px; font-weight: 700;
    color: var(--ink-strong);
    letter-spacing: -0.01em;
  }
  .holder__credentials { font-size: 20px; font-weight: 500; }
  .holder__role { margin-top: 2px; font-size: 17px; font-weight: 400; }
  .holder__rule {
    width: 43px; height: 2px;
    background: var(--rule);
    margin-top: 10px;
  }
  .contact {
    position: absolute;
    left: 38px; top: 388px;
    font-size: 18px; font-weight: 400;
    line-height: 31px;
    white-space: nowrap;
  }
  .contact__line { display: flex; align-items: center; gap: 5px; }
  .contact__icon { width: 15px; height: 15px; flex: none; }
  .contact__sep { margin: 0 5px; }
</style>
</head>
<body>

  <section class="card card--front">
    <div class="brand-square"></div>
    <div class="brand-frame"><div class="brand-name">OSTREL APPRAISALS</div></div>
  </section>

  <section class="card card--back">
    <div class="brand-square"></div>
    <div class="brand-frame"><div class="brand-name">OSTREL APPRAISALS</div></div>

    <div class="holder">
      <div class="holder__name">MARTEN DEKKER <span class="holder__credentials">CFA, ASA, RV</span></div>
      <div class="holder__role">Managing Director</div>
      <div class="holder__rule"></div>
    </div>

    <div class="contact">
      <div class="contact__line">
        <svg class="contact__icon" viewBox="0 0 16 16" aria-hidden="true">
          <path d="M4 1.5l2.3 3-1.4 1.6c.8 2 2.4 3.6 4.4 4.4l1.6-1.4 3 2.3-1.2 2.6C7.5 14 2 8.5 1.5 3z" fill="none" stroke="#777" stroke-width="1.4" stroke-linejoin="round"/>
        </svg>
        <span>+31 (0)70 555 0142</span>
        <span class="contact__sep">|</span>
        <svg class="contact__icon" viewBox="0 0 16 16" aria-hidden="true">
          <rect x="1.5" y="3.5" width="13" height="10" fill="none" stroke="#777" stroke-width="1.4"/>
          <path d="M1.5 3.5l6.5 5.5 6.5-5.5" fill="none" stroke="#777" stroke-width="1.4"/>
        </svg>
        <span>mdekker@ostrelappraisals.com</span>
        <span class="contact__sep">|</span>
        <svg class="contact__icon" viewBox="0 0 16 16" aria-hidden="true">
          <circle cx="8" cy="8" r="6.5" fill="none" stroke="#777" stroke-width="1.3"/>
          <ellipse cx="8" cy="8" rx="2.8" ry="6.5" fill="none" stroke="#777" stroke-width="1.1"/>
          <path d="M1.5 8h13M2.6 4.6h10.8M2.6 11.4h10.8" stroke="#777" stroke-width="1.1"/>
        </svg>
        <span>www.ostrelappraisals.com</span>
      </div>
      <div class="contact__line">Molenvlietkade 27 4817 KT Leiden The Netherlands</div>
    </div>
  </section>

</body>
</html>
```